Online Psychology Practice needs business cards.

Online Psychology service needs business cards. Have own logo- please see uploaded. I have other file formats if you need (not sure one needed?)

Details for Business Card:
Helena Marchetti
Clinical Psychologist BPsych, BPsych (Hons), MPsych (Clin), MAPS
T: 0439627015 | F: 08 73615204
E: hello@brightwatertelehealthcounselling.com.au
W: brightwatertelehealthcounselling.com.au

Industry/Entity Type

Health

Contact Information for Business Card

Logo plus details above (couldn't write in this section)

```html
<!DOCTYPE html>
<html lang="en">
<head>
<meta charset="utf-8">
<title>Brightwater Telehealth Counselling – Business Cards</title>
<link href="https://fonts.googleapis.com/css2?family=Cinzel:wght@600&family=Roboto:wght@400&display=swap" rel="stylesheet">
<style>
  :root {
    --navy: #1d4a73;
    --teal: #1f7f9c;
    --ink: #333333;
    --paper: #ffffff;
    --backdrop: #e9e9ea;
  }
  * { margin: 0; padding: 0; box-sizing: border-box; }
  html, body { width: 1200px; height: 1200px; overflow: hidden; }
  body {
    background: var(--backdrop);
    font-family: "Roboto", Arial, sans-serif;
    position: relative;
  }
  .card {
    position: absolute;
    width: 594px;
    height: 346px;
    background: var(--paper);
    border-radius: 18px;
    overflow: hidden;
  }
  .card--front { left: 298px; top: 200px; }
  .card--back  { left: 292px; top: 637px; }

  .brand {
    position: absolute;
    text-align: center;
    font-family: "Cinzel", Georgia, serif;
    font-weight: 600;
    color: var(--navy);
    line-height: 1.15;
  }
  .brand__dot {
    display: block;
    margin: 0 auto 14px;
    border-radius: 50%;
    background: var(--navy);
  }
  .card--front .brand { left: 0; right: 0; top: 70px; font-size: 30px; }
  .card--front .brand__dot { width: 64px; height: 64px; }
  .card--back .brand { left: 20px; width: 280px; top: 40px; font-size: 22px; }
  .card--back .brand__dot { width: 54px; height: 54px; margin-bottom: 16px; }

  .front__url {
    position: absolute;
    left: 0; right: 0; top: 295px;
    text-align: center;
    font-size: 15px;
    color: var(--ink);
  }
  .front__band {
    position: absolute;
    left: 0; right: 0; bottom: 0;
    height: 10px;
    background: linear-gradient(90deg, var(--navy) 0 50%, var(--teal) 50% 100%);
  }

  .person {
    position: absolute;
    right: 30px; top: 40px;
    text-align: right;
  }
  .person__name {
    font-family: "Cinzel", Georgia, serif;
    font-weight: 600;
    font-size: 22px;
    letter-spacing: 1px;
    color: var(--ink);
  }
  .person__role { font-size: 14.5px; color: var(--teal); margin-top: 6px; }
  .person__creds { font-size: 13px; color: var(--ink); line-height: 1.5; margin-top: 2px; }

  .back__wave { position: absolute; left: 0; top: 0; }

  .contacts {
    position: absolute;
    right: 26px; top: 244px;
    list-style: none;
    color: #ffffff;
    font-size: 14.5px;
    line-height: 21.5px;
    text-align: right;
  }
  .contacts li { display: flex; justify-content: flex-end; align-items: center; gap: 8px; }
  .contacts svg { width: 13px; height: 13px; flex: none; }
</style>
</head>
<body>

<section class="card card--front">
  <div class="brand">
    <span class="brand__dot"></span>
    Brightwater<br>Telehealth Counselling
  </div>
  <p class="front__url">www.brightwatertelehealthcounselling.com.au</p>
  <div class="front__band"></div>
</section>

<section class="card card--back">
  <div class="brand">
    <span class="brand__dot"></span>
    Brightwater<br>Telehealth Counselling
  </div>

  <div class="person">
    <p class="person__name">HELENA MARCHETTI</p>
    <p class="person__role">Clinical Psychologist</p>
    <p class="person__creds">BPsych, BPsych (Hons),<br>MPsych (Clin), MAPS</p>
  </div>

  <svg class="back__wave" width="594" height="346" viewBox="0 0 594 346">
    <defs>
      <linearGradient id="waveFill" x1="0" y1="0" x2="1" y2="0">
        <stop offset="0" stop-color="#1d4a73"/>
        <stop offset="1" stop-color="#1f7f9c"/>
      </linearGradient>
    </defs>
    <path d="M0,240 C140,270 250,300 380,238 C470,196 540,182 594,172 L594,346 L0,346 Z" fill="url(#waveFill)"/>
    <path d="M35,250 C160,280 260,285 390,228 C470,194 540,180 594,176" fill="none" stroke="#ffffff" stroke-width="6"/>
    <path d="M0,220 C120,250 250,275 380,215 C470,175 540,162 594,150" fill="none" stroke="#1f7f9c" stroke-width="3"/>
  </svg>

  <ul class="contacts">
    <li>04 39627015
      <svg viewBox="0 0 16 16"><path d="M2 6 C2 3 14 3 14 6 L11 7 L10 5 L6 5 L5 7 Z M4 8 H12 L13 13 H3 Z" fill="#fff"/></svg></li>
    <li>08 73615204
      <svg viewBox="0 0 16 16"><path d="M2 6 C2 3 14 3 14 6 L11 7 L10 5 L6 5 L5 7 Z M4 8 H12 L13 13 H3 Z" fill="#fff"/></svg></li>
    <li>brightwatertelehealthcounselling.com.au
      <svg viewBox="0 0 16 16"><circle cx="8" cy="8" r="6.5" fill="none" stroke="#fff" stroke-width="1.5"/><ellipse cx="8" cy="8" rx="3" ry="6.5" fill="none" stroke="#fff" stroke-width="1.2"/><path d="M1.5 8 H14.5" stroke="#fff" stroke-width="1.2"/></svg></li>
    <li>hello@brightwatertelehealthcounselling.com.au
      <svg viewBox="0 0 16 16"><rect x="1" y="3" width="14" height="10" fill="#fff"/><path d="M1 3 L8 9 L15 3" fill="none" stroke="#1f7f9c" stroke-width="1.3"/></svg></li>
  </ul>
</section>

</body>
</html>
```